Print on top the name of the company: (Or Similar)
Bellhaven Cleaning & Disinfecting
Because your standards aren't standard.

We adhere to ALL FHB guidelines for both residential and commercial cleaning.

Infection Control is our ultimate goal.

Instructions:
Opening a residential and commercial cleaning and disinfecting company in south Florida.

Targeting high-end residential clients, commercial and healthcare facilities, specializing in Ambulatory Care Guidelines. With a concentration and expertise in targeting Covid 19 and other transmissible pathogens.

TWLR trained.
Owned and operated by a licensed BSN Registered Nurse specially ​trained in Infection Control Prevention with over 25 years experience. Over two decades in Ambulatory Surgery Center Administration, Director of Nursing and Infection Control Prevention ad Consulting.

Looking to create a business flier that emphasizes Cleaning & Disinfection
along with the standard expectation for residential and Commercial cleaning services

Target Market(s)

Residential & Commercial

Font styles to use
Decorative

Requirements
Must have
• A checklist for cleaning services

```html
<!DOCTYPE html>
<html lang="en">
<head>
<meta charset="utf-8">
<title>Bellhaven Cleaning &amp; Disinfecting — Flyer</title>
<link rel="stylesheet" href="https://fonts.googleapis.com/css2?family=Oswald:wght@500;600;700&display=swap">
<style>
  :root {
    --navy: #1d3a6b;
    --navy-deep: #142c55;
    --red: #ee3032;
    --yellow: #ffee1f;
    --ink: #111111;
    --white: #ffffff;
    --mist: #eef3f7;
    --sky: #b9d6ee;
    --suit: #aebab4;
    --page: #ffffff;
  }
  * { box-sizing: border-box; margin: 0; padding: 0; }
  html, body { width: 1200px; height: 1200px; overflow: hidden; background: var(--page); }
  .flyer {
    position: absolute; left: 176px; top: 0; width: 848px; height: 1200px;
    overflow: hidden; font-family: "Oswald", sans-serif; background: var(--mist);
  }
  .hero-photo {
    position: absolute; left: 0; top: 0; width: 848px; height: 452px;
    background: linear-gradient(100deg, var(--navy-deep) 0%, var(--navy) 45%, #2a4a7c 75%, var(--navy-deep) 100%);
  }
  .scene-photo {
    position: absolute; left: 0; top: 452px; width: 848px; height: 748px;
    background: linear-gradient(180deg, #f4f6f8 0%, #e9eef2 60%, #dfe5ea 100%);
  }
  .window-glow {
    position: absolute; left: 440px; top: 403px; width: 230px; height: 630px;
    background: linear-gradient(90deg, rgba(185,214,238,0) 0%, var(--sky) 60%, #9fc6e6 100%);
  }
  .technician-photo {
    position: absolute; left: 600px; top: 403px; width: 248px; height: 712px;
    background: linear-gradient(180deg, #9aa7a2 0%, var(--suit) 40%, #c4ccd0 75%, #dde3e6 100%);
  }
  .spray-photo {
    position: absolute; left: 0; top: 840px; width: 100px; height: 360px;
    background: linear-gradient(180deg, #e8ecef 0%, #d6dde3 50%, #eef1f3 100%);
  }
  .headline-panel {
    position: absolute; left: 66px; top: 403px; width: 600px; height: 400px;
    background: rgba(255,255,255,0.55);
  }
  .brand {
    position: absolute; left: 58px; top: 40px;
    color: var(--white); font-weight: 700; font-size: 80px; line-height: 86px;
    letter-spacing: 1px; text-transform: uppercase;
  }
  .tagline {
    position: absolute; left: 64px; top: 306px;
    color: var(--white); font-weight: 700; font-size: 22px; letter-spacing: 1.6px;
    text-transform: uppercase;
  }
  .headline {
    position: absolute; left: 95px; top: 452px;
    color: var(--red); font-weight: 700; font-size: 76px; line-height: 81.5px;
    letter-spacing: 1px; text-transform: uppercase;
  }
  .services {
    position: absolute; left: 66px; top: 804px; width: 592px; height: 233px;
    background: rgba(255,255,255,0.72);
  }
  .service-col { position: absolute; top: 22px; }
  .service-col.commercial { left: 62px; }
  .service-col.residential { left: 321px; }
  .service-col h2 {
    font-weight: 700; font-size: 19px; letter-spacing: 1.2px; color: var(--ink);
    text-transform: uppercase;
  }
  .service-col ul { list-style: none; margin-top: 30px; }
  .service-col.residential ul { margin-top: 26px; }
  .service-col li {
    position: relative; padding-left: 12px;
    font-weight: 600; font-size: 15px; line-height: 18.8px; letter-spacing: 0.6px; color: var(--ink);
  }
  .service-col li::before {
    content: ""; position: absolute; left: 0; top: 7px; width: 5px; height: 5px;
    border-radius: 50%; background: var(--red);
  }
  .cta {
    position: absolute; left: 414px; top: 1058px; width: 434px; height: 119px;
    background: var(--red); border-radius: 8px 0 0 8px;
    text-align: right; padding: 12px 48px 0 0;
  }
  .cta-line {
    color: var(--white); font-weight: 700; font-size: 25px; line-height: 30px;
    letter-spacing: 1.4px; text-transform: uppercase;
  }
  .cta-phone {
    color: var(--yellow); font-weight: 700; font-size: 38px; line-height: 50px; letter-spacing: 0.5px;
  }
</style>
</head>
<body>
  <main class="flyer">
    <div class="hero-photo" role="img" aria-label="Dim hospital corridor with a cleaning cart, tinted navy blue"></div>
    <div class="scene-photo" role="img" aria-label="Bright clinical room interior"></div>
    <div class="window-glow" role="img" aria-label="Soft blue light from a window"></div>
    <div class="spray-photo" role="img" aria-label="Gloved hand wiping a surface with a spray bottle"></div>
    <div class="technician-photo" role="img" aria-label="Technician in protective suit and respirator fogging disinfectant"></div>
    <div class="headline-panel"></div>

    <h1 class="brand">Bellhaven<br>Cleaning<br>&amp; Disinfecting</h1>
    <p class="tagline">Because your standards aren’t standard.</p>

    <p class="headline">Infection<br>Control<br>is our<br>ultimate goal.</p>

    <section class="services">
      <div class="service-col commercial">
        <h2>Commercial</h2>
        <ul>
          <li>Janitorial</li>
          <li>Offices</li>
          <li>Floor cleaning</li>
          <li>Move-ins</li>
          <li>Move-outs</li>
          <li>Constructions clean-ups</li>
          <li>Estate clean-outs</li>
        </ul>
      </div>
      <div class="service-col residential">
        <h2>Residential</h2>
        <ul>
          <li>House cleaning</li>
          <li>Before and after party</li>
          <li>Move-ins</li>
          <li>Move-outs</li>
          <li>Holiday cleaning</li>
          <li>Seasonal cleaning</li>
          <li>Carpet cleaning</li>
          <li>Deodorizing and sanitizing</li>
        </ul>
      </div>
    </section>

    <aside class="cta">
      <p class="cta-line">Call us to find out how you</p>
      <p class="cta-line">can save money this month!</p>
      <p class="cta-phone">(415) 555 0142</p>
    </aside>
  </main>
</body>
</html>
```